Web Site Redesign

We operate a data centre facility specialing in colocation and Fibre optic connectivity (i.e. point to point fibre services and internet over fibre).

We have an existing site located at www.norvalex.example however this is very very tired and requires a redesign. We are looking for a fresh new design that will be appealing to potential customers.

The Company name is Norva eX and the primary corporate colour is bright red with secondary colours of white, grey and black. Specific bright red can be seen in attached company logo.

Website needs to be modern, clean and professional representing our premium colocation and fibre provider branding.

Our company slogan is : safe. secure. reliable

We will provide feedback regardless of the quality of the design to ensure a better outcome for all parties.

Please feel free to contact us if you have any questions.

# The designer can use placeholder images or feel free to use any/all or none of the attached images
# The designer can use sample filler text

Target Market(s)

Technical IT Professionals as well C level executives (i.e. CEO's, CIO).

Industry/Entity Type

Internet

Requirements
Must have
• clean design
Nice to have
• A sidebar with two sections. 1 for current promo and 1 for "Let us call you back/contact you"
Should not have
• Clutter

```html
<!DOCTYPE html>
<html lang="en">
<head>
<meta charset="utf-8">
<title>Norva eX — Data Centre</title>
<link href="https://fonts.googleapis.com/css2?family=Open+Sans:wght@400;600;700&display=swap" rel="stylesheet">
<style>
:root{
  --red:#d4161a;
  --grey-dark:#2f2f2f;
  --text:#3a3a3a;
  --amber:#fbaa00;
  --amber-light:#ffcd3a;
  --white:#fff;
  --link-yellow:#ffd200;
}
*{box-sizing:border-box;margin:0;padding:0}
html,body{width:969px;height:1200px;overflow:hidden;background:var(--white)}
body{position:relative;font-family:"Open Sans",sans-serif;color:var(--text)}
.abs{position:absolute}

.brand{left:48px;top:112px;width:160px}
.brand-name{display:flex;align-items:center;gap:6px;font-size:27px;font-weight:600;color:var(--grey-dark);letter-spacing:-.5px;line-height:34px}
.brand-name .mark{width:12px;height:12px;background:var(--red)}
.brand-tag{font-size:12px;color:var(--grey-dark);margin-top:4px;line-height:14px}

.slogan{right:49px;top:8px;font-size:17px;color:#444;display:flex;align-items:center;gap:7px}
.slogan i{width:5px;height:5px;background:#444;display:block}
.address{right:48px;top:110px;text-align:right;font-size:9.5px;line-height:11.5px;color:#000;font-weight:600;font-style:normal}

.nav{left:0;top:182px;width:968px;height:48px;border-radius:7px;background:linear-gradient(#6a6a6a,#3a3a3a 45%,#262626)}
.nav a{color:var(--white);text-decoration:none;font-size:15px;height:48px;display:flex;align-items:center;position:absolute;top:0;white-space:nowrap}
.nav a.active{background:#454545;width:96px;justify-content:center;left:50px}

.hero{left:50px;top:280px;width:871px;height:241px;border-radius:8px;overflow:hidden;background:linear-gradient(180deg,#d0140f,#9c0a0a 55%,#6a0506)}
.hero-photo{position:absolute;left:440px;top:0;width:431px;height:241px;background:linear-gradient(180deg,#4a5270 0%,#6a6f88 12%,#2a2626 30%,#3a3636 60%,#d9d9dc 80%,#f0f0f2 100%)}
.hero-photo::before{content:"";position:absolute;left:0;top:0;width:110px;height:100%;background:linear-gradient(90deg,#a00c0c 0%,rgba(160,12,12,.85) 30%,rgba(160,12,12,0) 100%)}
.hero h1{position:absolute;left:15px;top:18px;font-size:33px;font-weight:400;color:var(--white);text-shadow:2px 2px 2px #222;white-space:nowrap}
.hero p{position:absolute;left:14px;font-size:16px;line-height:19.5px;color:var(--white);white-space:nowrap}

.intro{left:55px;top:556px;font-size:13.6px;line-height:16.2px;color:var(--text);white-space:nowrap}
.intro p{margin-bottom:16px}

.notice{left:49px;top:835px;width:292px;height:122px;background:var(--amber)}
.notice-head{height:24px;background:#3e3e3e;color:var(--link-yellow);font-size:14px;padding:3px 5px;box-shadow:0 2px 3px rgba(0,0,0,.4)}
.notice-title{color:var(--white);font-size:14px;margin:10px 0 0 6px}
.notice-link{display:block;font-size:11px;color:#222;margin:3px 0 0 6px}
.notice-more{position:absolute;right:8px;bottom:4px;font-size:11px;font-weight:700;color:var(--white)}

.enquiry{left:663px;top:545px;width:244px;height:412px;background:linear-gradient(#5a5a5a,#2c2c2c);color:var(--white)}
.enquiry-tab{left:647px;top:552px;width:273px;height:43px;background:linear-gradient(var(--amber-light),var(--amber));font-size:16px;color:#222;padding:14px 0 0 23px}
.enquiry > *{position:absolute;left:8px}
.enquiry-intro{top:58px;font-size:13px;line-height:14.5px;white-space:nowrap}
.enquiry label{font-size:13px;line-height:15px}
.enquiry .field{width:154px;height:22px;background:var(--white)}
.enquiry .area{width:227px;height:104px;background:var(--white)}
.send{left:162px !important;top:387px;width:73px;height:16px;border-radius:8px;background:var(--amber);color:#222;font-size:12px;text-align:center;line-height:16px}

.footer{left:49px;top:990px;width:872px;height:168px;background:linear-gradient(#5a5a5a,#2b2b2b);color:var(--white)}
.footer h2{position:absolute;top:16px;font-size:19px;font-weight:700}
.footer ul{position:absolute;list-style:none;font-size:11px}
.footer li{display:flex;align-items:center;gap:7px;height:19.5px}
.footer li::before{content:"";width:5px;height:5px;background:#ddd}
.partners li{color:#ddd}
.contacts{position:absolute;left:672px;top:57px;font-size:11px;line-height:13px}
.contacts span{color:#ccc;display:block}
</style>
</head>
<body>

<header>
  <div class="abs brand">
    <div class="brand-name"><span class="mark"></span>Norva eX</div>
    <div class="brand-tag">Innovate IT Solutions</div>
  </div>
  <div class="abs slogan">Safe <i></i> Secure <i></i> Reliable</div>
  <address class="abs address">
    Norva eX<br>14 Harbour Lane<br>Perth WA 6000<br>+61 8 9000 4120<br>Mon to Fri 7:00 am to 7:00 pm
  </address>
</header>

<nav class="abs nav">
  <a class="active" href="#">Home</a>
  <a href="#" style="left:157px">About Us</a>
  <a href="#" style="left:258px">Facilities</a>
  <a href="#" style="left:368px;top:-2px">Bussines Continuity</a>
  <a href="#" style="left:549px;top:-1px">Services</a>
  <a href="#" style="left:646px;top:-1px">Partners</a>
  <a href="#" style="left:740px">Web Mail</a>
  <a href="#" style="left:831px;top:-1px">Contact Us</a>
</nav>

<section class="abs hero">
  <div class="hero-photo" role="img" aria-label="Rows of server racks in a data centre hall"></div>
  <h1>Welcome to Norva eX!</h1>
  <p style="top:81px">A world class data centre in the safest place on Earth.</p>
  <p style="top:120px">With a centrally located data centre in the heart of the<br>Perth CBD, Norva eX is excellently positioned to assist<br>with your critical IT requirements.</p>
</section>

<main class="abs intro">
  <p>The CBD facility features overlapping power grids, redundant power supplies<br>and comprehensively maintained infrastructure,&nbsp; providing excellent levels of<br>protection for your critical IT equipment.</p>
  <p>The State's newest and most technologically advanced data centre<br>is also now open in Belmont, a convenient 5.5 km's from the CBD<br>providing a perfect location for either production sites,<br>&nbsp;or DR infrastructure.</p>
  <p>From Government departments to large corporations to SME's,<br>Norva eX is the ideal company to assist with your colocation requirements.<br>With warm racks already provisioned, you can begin using the data centre<br>almost immediately.</p>
  <p>Call us today to see how we can help meet your needs.</p>
</main>

<aside class="abs notice">
  <div class="notice-head">Important Announcements &gt;&gt;</div>
  <div class="notice-title">Transaction Notification:</div>
  <a class="notice-link" href="#">norvalex.example/norvalex/NeX_DC.pdf</a>
  <a class="notice-more" href="#">read more</a>
</aside>

<aside class="abs enquiry">
  <p class="enquiry-intro">Talk to us about designing<br>a solution to meet your<br>needs.</p>
  <label style="top:128px">Name :</label><div class="field" style="top:145px"></div>
  <label style="top:172px">E-mail:</label><div class="field" style="top:187px"></div>
  <label style="top:216px">Phone :</label><div class="field" style="top:231px"></div>
  <label style="top:257px">Message:</label><div class="area" style="top:274px"></div>
  <div class="send">send</div>
</aside>
<div class="abs enquiry-tab">Need more Info ?</div>

<footer class="abs footer">
  <h2 style="left:26px">Partners :</h2>
  <ul class="partners" style="left:26px;top:57px">
    <li>Brightline Networks</li><li>Corvel</li><li>Voltaline</li><li>Moss Consultants</li>
  </ul>
  <h2 style="left:387px">Services:</h2>
  <ul style="left:387px;top:53px">
    <li>Internet Options</li><li>Fibre</li><li>Managed Services</li><li>Vizualization</li>
  </ul>
  <h2 style="left:667px">Contact Details:</h2>
  <div class="contacts">
    Sales:<span>sales@norvalex.example</span>
    Technical Support:<span>noc@norvalex.example</span>
    Account Enquiries:<span>accounts@norvalex.example</span>
  </div>
</footer>

</body>
</html>
```